Newlyweds banner image for wedding reception

Banner with the words “The Newlyweds” (No quotations) in an elegant and thick (bold) font. Font must be easy to read. Gold or silver letters. Words should easily be edited so that we have the option to print in gold or silver. No background. Image must have source file as well as be delivered as a png with a transparent background. Image will be printed in a horizontal orientation. Must be 300 Dpi for printing. Image must not lose any quality and remain crisp and sharp when expanded and printed to a size of up to 6 feet wide and 2 feet tall. Be creative but we are looking for an elegant option. First and foremost.

Target Market(s)

Wedding planners, brides planning wedding and reception

Industry/Entity Type

Wedding decoration

Colors

Designer to choose colors to be used in the design.

Requirements
Must have
• Gold or Silver letters
Should not have
• Do not mix colors

```html
<!DOCTYPE html>
<html lang="en">
<head>
<meta charset="UTF-8">
<title>The Newlyweds – Reception Banner</title>
<link rel="stylesheet" href="https://fonts.googleapis.com/css2?family=Cinzel:wght@700&display=swap">
<style>
  :root {
    --backdrop: #1c1c1c;
    --paper: #ffffff;
    --paper-shade: #ececec;
    --gold-deep: #7a5818;
    --gold-mid: #c9a22e;
    --gold-light: #f0d676;
    --gold-bronze: #96743a;
    --wash-tone: #e8d9ad;
    --wash-light: #fbf3d2;
  }
  * { margin: 0; padding: 0; box-sizing: border-box; }
  html, body {
    width: 1200px;
    height: 675px;
    overflow: hidden;
    background: var(--backdrop);
  }
  .canvas {
    position: relative;
    width: 1200px;
    height: 675px;
    display: flex;
    align-items: center;
    justify-content: center;
  }
  .banner {
    position: relative;
    width: 1080px;
    height: 360px;
    background: linear-gradient(90deg, var(--paper-shade) 0%, var(--paper) 45%, var(--paper) 100%);
    overflow: hidden;
  }
  .banner__wash {
    position: absolute;
    left: 14%;
    top: 8%;
    width: 78%;
    height: 92%;
    background:
      radial-gradient(ellipse 45% 55% at 35% 55%, var(--wash-tone) 0%, rgba(232,217,173,0.6) 55%, rgba(232,217,173,0) 100%),
      radial-gradient(ellipse 30% 45% at 80% 60%, var(--wash-light) 0%, rgba(251,243,210,0) 100%);
  }
  .banner__frame-outer {
    position: absolute;
    inset: 12px;
    border: 3px solid var(--gold-mid);
  }
  .banner__frame-inner {
    position: absolute;
    inset: 22px;
    border: 1.5px solid var(--gold-mid);
  }
  .banner__title {
    position: absolute;
    inset: 0;
    width: 100%;
    height: 100%;
  }
  .banner__title text {
    font-family: 'Cinzel', serif;
    font-weight: 700;
    font-size: 104px;
    letter-spacing: 2px;
    paint-order: stroke fill;
    stroke: var(--paper);
    stroke-width: 6px;
    stroke-linejoin: round;
  }
</style>
</head>
<body>
  <main class="canvas">
    <section class="banner">
      <div class="banner__wash" role="img" aria-label="Soft gold watercolour wash behind the title"></div>
      <div class="banner__frame-outer"></div>
      <div class="banner__frame-inner"></div>
      <svg class="banner__title" viewBox="0 0 1080 360" aria-labelledby="banner-title">
        <defs>
          <linearGradient id="gold-foil" x1="0" y1="0" x2="0" y2="1">
            <stop offset="0%" stop-color="var(--gold-bronze)"/>
            <stop offset="30%" stop-color="var(--gold-light)"/>
            <stop offset="50%" stop-color="var(--gold-deep)"/>
            <stop offset="75%" stop-color="var(--gold-mid)"/>
            <stop offset="100%" stop-color="var(--gold-light)"/>
          </linearGradient>
        </defs>
        <text id="banner-title" x="540" y="218" text-anchor="middle" fill="url(#gold-foil)">THE NEWLYWEDS</text>
      </svg>
    </section>
  </main>
</body>
</html>
```